Willow’s Lantern - Childhood Cancer Journey

In 2019, Corbin, my five-year-old, was diagnosed with stage 4 kidney cancer.

From the beginning, I said God would do his part, the doctors will do theirs, and I would do mine to save my son.

Diving into Christian beliefs and research, I learned and applied major shifts in everything we didn’t. Pulling invaluable information from fields like alternative cancer treatments coupled with Tall Reed study, Longevity, Biohacking, Functional Medicine, and microbiome.

Corbin when from stage 4 to cancer-free in 8 months. The journey is and was very difficult, but we’ve learned and been able to help countless others.

Industry/Entity Type

Health, Wellness, Mindset, Adversity

Requirements
Nice to have
• Bright with feelings of warmth

```html
<!DOCTYPE html>
<html lang="en">
<head>
<meta charset="utf-8">
<title>Willow’s Lantern – Book Cover</title>
<link href="https://fonts.googleapis.com/css2?family=Comfortaa:wght@400;500&family=Open+Sans:wght@700;800&display=swap" rel="stylesheet">
<style>
  :root {
    --leaf-dark: #3d5a3c;
    --leaf-mid: #7fa38a;
    --leaf-light: #c9d9cf;
    --berry-deep: #c8261d;
    --berry-mid: #e8452c;
    --berry-light: #f6a58a;
    --heart-orange: #f0561f;
    --photo-warm: #b8866d;
    --photo-dark: #5d4338;
    --white: #ffffff;
  }
  html, body {
    margin: 0;
    padding: 0;
    overflow: hidden;
    background: #e9e9e9;
  }
  .cover {
    position: relative;
    width: 750px;
    height: 1200px;
    overflow: hidden;
    background: var(--leaf-mid);
  }
  .cover-art {
    position: absolute;
    inset: 0;
    width: 750px;
    height: 1200px;
  }
  .book-title {
    position: absolute;
    left: 0;
    top: 760px;
    width: 750px;
    margin: 0;
    font-family: "Comfortaa", sans-serif;
    font-weight: 400;
    color: var(--white);
    font-size: 104px;
    line-height: 112px;
    letter-spacing: -1px;
  }
  .book-title .line-one { display: block; padding-left: 220px; }
  .book-title .line-two { display: block; padding-left: 205px; }
  .book-subtitle {
    position: absolute;
    left: 60px;
    top: 1066px;
    width: 630px;
    margin: 0;
    text-align: center;
    font-family: "Open Sans", sans-serif;
    font-weight: 700;
    font-size: 17.5px;
    line-height: 22px;
    color: var(--white);
  }
  .book-author {
    position: absolute;
    left: 0;
    top: 1152px;
    width: 750px;
    margin: 0;
    text-align: center;
    font-family: "Open Sans", sans-serif;
    font-weight: 800;
    font-size: 24px;
    letter-spacing: 3px;
    color: var(--white);
  }
</style>
</head>
<body>
<main class="cover">
  <svg class="cover-art" viewBox="0 0 750 1200" xmlns="http://www.w3.org/2000/svg">
    <defs>
      <linearGradient id="leafTone" x1="0" y1="0" x2="1" y2="1">
        <stop offset="0" stop-color="var(--leaf-light)"/>
        <stop offset="0.5" stop-color="var(--leaf-mid)"/>
        <stop offset="1" stop-color="var(--leaf-dark)"/>
      </linearGradient>
      <radialGradient id="berryTone" cx="0.5" cy="0.45" r="0.7">
        <stop offset="0" stop-color="var(--berry-light)"/>
        <stop offset="0.45" stop-color="var(--berry-mid)"/>
        <stop offset="1" stop-color="var(--berry-deep)"/>
      </radialGradient>
      <linearGradient id="photoTone" x1="0" y1="0" x2="1" y2="1">
        <stop offset="0" stop-color="var(--photo-warm)"/>
        <stop offset="1" stop-color="var(--photo-dark)"/>
      </linearGradient>
      <clipPath id="heartWindow">
        <path d="M375 620 C300 540 135 440 125 300 C118 200 185 150 255 150 C315 150 355 190 375 235 C395 190 435 150 495 150 C565 150 632 200 625 300 C615 440 450 540 375 620 Z"/>
      </clipPath>
    </defs>

    <rect class="leaf-backdrop" x="0" y="0" width="750" height="760" fill="url(#leafTone)" role="img" aria-label="Close-up photograph of green leafy vegetables with water droplets"/>

    <path class="berry-backdrop" d="M0 600 C120 560 250 610 375 700 C500 610 630 560 750 600 L750 1200 L0 1200 Z" fill="url(#berryTone)" role="img" aria-label="Close-up photograph of sliced strawberry halves"/>

    <path class="heart-frame" d="M375 660 C280 570 95 460 85 290 C78 160 170 68 270 68 C320 68 355 95 375 125 C395 95 430 68 480 68 C580 68 672 160 665 290 C655 460 470 570 375 660 Z" fill="var(--heart-orange)"/>

    <rect class="heart-photo" x="115" y="150" width="520" height="480" fill="url(#photoTone)" clip-path="url(#heartWindow)" role="img" aria-label="Photograph of a smiling father in a cap hugging his young son wearing a face mask"/>
  </svg>

  <h1 class="book-title">
    <span class="line-one">Willow’s</span>
    <span class="line-two">Lantern</span>
  </h1>

  <p class="book-subtitle">A Loving Father, Determined to Guide His Cancer-Stricken Son’s Journey to a Cure, Discovers the Tall Reed Protocol of Nourishing the Body to Optimum Health</p>

  <p class="book-author">REID CALLOWAY</p>
</main>
</body>
</html>
```